Want a DL Flyer designed for mailout, with the following info. Please see the website www.ledgerbrightco.com.au for any other info.
Content:
EVERYTHING YOU NEED FROM AN ACCOUNTANT
(tick) Value for money
(tick) Mobile visits to your farm or business
(tick) Fixed Fees Agreed Upfront
(tick) Advice tailored to your circumstances
(tick) Help to grow your business
(tick) Talk directly to your accountant, the person who knows you
(tick) Small business & Primary Producer Specialists
+ MORE.......TALLYWELL GROUP. YOU'RE MORE THAN A NUMBER WITH US.
Director: Gordon Pellew CPA | Associate: Soraya Finch CPA
Call (07) 4519 2386 www.ledgerbrightco.com.au PO Box 827 Dalby Qld 4405

```html
<!DOCTYPE html>
<html lang="en">
<head>
<meta charset="utf-8">
<title>Tallywell Group – DL Flyer</title>
<link rel="stylesheet" href="https://fonts.googleapis.com/css2?family=Oswald:wght@600;700&family=Quicksand:wght@500;700&display=swap">
<style>
  :root {
    --red: #e0181f;
    --red-deep: #c9161c;
    --grey-band: #c4c4c4;
    --grey-foot: #b5b5b6;
    --ink: #111111;
    --white: #ffffff;
    --backdrop: #3b3b3b;
    --photo-dark: #2c3b4e;
    --photo-light: #dfe4ea;
  }
  html, body { margin: 0; padding: 0; }
  body {
    width: 1200px; height: 1200px; overflow: hidden;
    background: var(--backdrop); position: relative;
    font-family: "Quicksand", sans-serif;
  }
  .flyer {
    position: absolute; left: 363px; top: 138px;
    width: 571px; height: 1174px;
    transform: scale(0.8); transform-origin: 0 0;
    background: var(--white); overflow: hidden;
    box-shadow: 0 6px 18px rgba(0,0,0,.45);
  }
  .brand {
    position: absolute; left: 0; right: 0; top: 0; height: 138px;
    display: flex; align-items: center; justify-content: center; gap: 12px;
  }
  .brand-square { width: 22px; height: 22px; background: var(--red); }
  .brand-name {
    font-family: "Quicksand", sans-serif; font-weight: 700;
    font-size: 30px; color: var(--red); letter-spacing: .5px;
  }
  .hero { position: absolute; left: 0; top: 138px; width: 571px; height: 429px; }
  .hero svg { position: absolute; inset: 0; }
  .hero-headline {
    position: absolute; left: 38px; top: 218px; margin: 0;
    font-family: "Oswald", sans-serif; font-weight: 700; color: var(--white);
    text-transform: uppercase; line-height: 1;
  }
  .hero-headline span { display: block; }
  .hl-sm { font-size: 34px; }
  .hl-lg { font-size: 60px; margin-top: 2px; }
  .hl-md { font-size: 33px; margin-top: 4px; }
  .offer { position: absolute; left: 36px; top: 585px; margin: 0; font-family: "Oswald", sans-serif; font-weight: 700; line-height: 1; }
  .offer-top { display: block; font-size: 36px; color: var(--ink); }
  .offer-bottom { display: block; font-size: 54px; color: var(--red); margin-top: 2px; }
  .rule { position: absolute; left: 54px; top: 676px; width: 419px; height: 2px; background: var(--ink); }
  .benefits { position: absolute; left: 44px; top: 684px; margin: 0; padding: 0; list-style: none; width: 510px; }
  .benefits li {
    position: relative; padding-left: 43px; font-size: 21px; font-weight: 500;
    color: var(--ink); line-height: 26px; margin-bottom: 8.5px;
  }
  .benefits li svg { position: absolute; left: 0; top: 5px; width: 24px; height: 20px; }
  .contact { position: absolute; left: 0; top: 953px; width: 571px; height: 158px; background: var(--red); color: var(--white); }
  .portrait {
    position: absolute; left: 33px; top: 15px; width: 126px; height: 126px;
    border-radius: 50%; border: 3px solid #d9d9d9; box-sizing: border-box;
    background: radial-gradient(circle at 50% 35%, #7fa0c4, #3e5f3a 75%);
  }
  .contact-lines { position: absolute; left: 184px; top: 20px; }
  .director { font-size: 23px; font-weight: 700; margin: 0 0 6px; }
  .contact-row { font-size: 18px; font-weight: 500; margin: 0 0 8px; display: flex; align-items: center; gap: 7px; }
  .footer { position: absolute; left: 0; top: 1111px; width: 571px; height: 63px; background: var(--grey-foot); }
  .web { position: absolute; left: 92px; top: 6px; display: flex; align-items: center; gap: 10px; font-size: 21px; font-weight: 500; color: var(--ink); }
</style>
</head>
<body>
<article class="flyer">
  <header class="brand">
    <span class="brand-square"></span>
    <span class="brand-name">Tallywell Group</span>
  </header>

  <section class="hero">
    <svg width="571" height="429" viewBox="0 0 571 429">
      <defs>
        <linearGradient id="tint" x1="0" y1="0" x2="1" y2="1">
          <stop offset="0" stop-color="#e2352a"/>
          <stop offset="1" stop-color="#e8402c"/>
        </linearGradient>
        <linearGradient id="photo" x1="0" y1="0" x2="1" y2="1">
          <stop offset="0" stop-color="var(--photo-light)"/>
          <stop offset=".55" stop-color="#9aa9b8"/>
          <stop offset="1" stop-color="var(--photo-dark)"/>
        </linearGradient>
      </defs>
      <rect width="571" height="429" fill="var(--red)"/>
      <polygon points="0,0 64,0 266,429 0,429" fill="url(#tint)" role="img" aria-label="Red-tinted photo of a desk with financial papers"/>
      <polygon points="64,0 136,0 361,429 266,429" fill="var(--grey-band)"/>
      <polygon points="206,0 571,0 571,381 406,381" fill="url(#photo)" role="img" aria-label="Photo of hands typing on a laptop showing a trading dashboard"/>
      <polygon points="406,381 571,381 571,397 414,397" fill="var(--grey-band)"/>
    </svg>
    <h1 class="hero-headline">
      <span class="hl-sm">You're</span>
      <span class="hl-lg">More</span>
      <span class="hl-lg">Than A</span>
      <span class="hl-md">Number with us.</span>
    </h1>
  </section>

  <h2 class="offer">
    <span class="offer-top">EVERYTHING YOU NEED</span>
    <span class="offer-bottom">FROM AN ACCOUNTANT</span>
  </h2>
  <div class="rule"></div>

  <ul class="benefits">
    <li><svg viewBox="0 0 24 20"><path d="M2 10l7 7L22 3" fill="none" stroke="var(--red)" stroke-width="4"/></svg>Value for money</li>
    <li><svg viewBox="0 0 24 20"><path d="M2 10l7 7L22 3" fill="none" stroke="var(--red)" stroke-width="4"/></svg>Mobile visits to your farm or business</li>
    <li><svg viewBox="0 0 24 20"><path d="M2 10l7 7L22 3" fill="none" stroke="var(--red)" stroke-width="4"/></svg>Fixed Fees Agreed Upfront</li>
    <li><svg viewBox="0 0 24 20"><path d="M2 10l7 7L22 3" fill="none" stroke="var(--red)" stroke-width="4"/></svg>Advice tailored to your circumstances</li>
    <li><svg viewBox="0 0 24 20"><path d="M2 10l7 7L22 3" fill="none" stroke="var(--red)" stroke-width="4"/></svg>Help to grow your business</li>
    <li><svg viewBox="0 0 24 20"><path d="M2 10l7 7L22 3" fill="none" stroke="var(--red)" stroke-width="4"/></svg>Talk directly to your accountant, the person who knows you</li>
    <li><svg viewBox="0 0 24 20"><path d="M2 10l7 7L22 3" fill="none" stroke="var(--red)" stroke-width="4"/></svg>Small business &amp; Primary Producer Specialists</li>
  </ul>

  <section class="contact">
    <div class="portrait" role="img" aria-label="Portrait photo of the director"></div>
    <div class="contact-lines">
      <p class="director">Director : Gordon Pellew CPA</p>
      <p class="contact-row">Associate : Soraya Finch CPA</p>
      <p class="contact-row">Call
        <svg width="24" height="24" viewBox="0 0 24 24"><circle cx="12" cy="12" r="11" fill="none" stroke="#f3a0a0" stroke-width="1.5"/><path d="M8 6.5c-1 1-1 3 1 6s4.5 4.5 6 4.5l1.5-1.5-2.2-2-1.3 1c-1-.5-2.5-2-3-3l1-1.3-2-2.2z" fill="#f3a0a0"/></svg>
        (07) 4519 2386</p>
      <p class="contact-row">
        <svg width="18" height="20" viewBox="0 0 18 20"><path d="M9 1a6 6 0 0 0-6 6c0 5 6 12 6 12s6-7 6-12a6 6 0 0 0-6-6z" fill="#f3a0a0"/><circle cx="9" cy="7" r="2.2" fill="var(--red)"/></svg>
        &nbsp;&nbsp;PO Box 827 Dalby Qld 4405</p>
    </div>
  </section>

  <footer class="footer">
    <div class="web">
      <svg width="22" height="22" viewBox="0 0 22 22" fill="none" stroke="var(--ink)" stroke-width="1.6"><circle cx="11" cy="11" r="9.5"/><ellipse cx="11" cy="11" rx="4.5" ry="9.5"/><path d="M1.5 11h19M3 6h16M3 16h16"/></svg>
      www.ledgerbrightco.com.au
    </div>
  </footer>
</article>
</body>
</html>
```